依頼詳細
今回は、トップページデザインの募集になります。
レスポンシブデザインのサイトで、bootstrap4を利用しコーディングする予定になります。
デザイン幅は2000px、コンテンツの幅はbootstrap4デフォルトの1110pxを基準としてください。ただし最近のデザインの流行を取りいれて、フルワイドや、1200~15000px程度の幅のコンテンツをバランスよくレイアウトしてください。
コンテンツ配置は基本12分割になります。がデザインによっては、多少逸脱してもかまいません。
念のため、サンプルのPSDデータを添付しますので、参照ください。

本文のフォントはゴシック系は游ゴシック、メイリオ、明朝系は遊明朝でお願いします。
飾り文字はフリーフォントか、googleフォントを利用してください。

メイン画像部分・グローバルメニューは、ワイド適用でお願いします。

資料上はサイト名(社名)や住所などは伏字にしております。ご提案時点ではそのまま作成をお願いします。当選確定後、本内容に修正をお願いいたします。

当選の方は、希望があれば引き続き下層ページの作成及びコーディング作業を依頼可能です。
不明点、質問などありましたらメッセージ等でご連絡ください。

・カラー
青系(爽やかなイメージ)

・掲載画像
必ず添付ファイルを使用してください。
また、雰囲気が合っていれば、指定外の画像を背景などに使用いただいてもOKです。

・その他
内容詳細に関しては、別添のExcel資料を参照してください。
ページ数
1ページ
希望イメージ
シンプル 複雑
単色 カラフル
暗い 明るい
日常 高級
遊び心 厳粛
未来的 伝統的
女性的 男性的
希望する色
青系、水色系
納品ファイル
• 高解像度JPG (.jpg)
• フォトショップ形式 (.psd)
補足説明
納品ファイルは、PDF及びクライアント表示確認用のJPGを準備お願いします。
■ 選んだ理由

今回は、贅沢さや豪華さをイメージさせる洗練された先進的なデザインを希望しており、見た目が大事な案件でした。
業界的に国内外問わず「サイトの見た目」をかなり重要視しているため、"見栄えのするデザイン"というところに重きを置いてクライアントとの折衝の結果、skytrailふじさわ様を選定させていただきました。

■ 提案者全員のお礼・コメント

どの案も制作意図を組んでいただきとてもよかったのですが、今回はskytrailふじさわ様を当選とさせていただきました。
皆様ご提案ありがとうございました。
今後ともご提案宜しくお願いいたします。

```html
<!DOCTYPE html>
<html lang="ja">
<head>
<meta charset="utf-8">
<title>○○○○○○○株式会社</title>
<link href="https://fonts.googleapis.com/css2?family=Montserrat:wght@300;400;600&family=Noto+Sans+JP:wght@400;500;700&display=swap" rel="stylesheet">
<style>
:root{
  --blue:#1565c8;
  --blue-dark:#0b4fa3;
  --sky:#3aa6e0;
  --teal:#1aa0b8;
  --text:#333;
  --muted:#777;
  --line:#cfd8e3;
  --white:#fff;
}
*{margin:0;padding:0;box-sizing:border-box}
html,body{width:1200px;height:3424px;overflow:hidden}
body{font-family:"Noto Sans JP",sans-serif;color:var(--text);background:var(--white);position:relative}
.en{font-family:"Montserrat",sans-serif}
.photo{position:absolute;display:block}

/* header */
.site-header{position:absolute;top:0;left:0;width:1200px;height:108px;background:var(--white)}
.brand{position:absolute;left:112px;top:14px;width:200px;height:76px;border:2px solid var(--line);background:#eef2f7;display:flex;align-items:center;justify-content:center;font-size:18px;font-weight:500;color:var(--blue-dark);text-align:center;line-height:1.3}
.util{position:absolute;right:60px;top:8px;display:flex;gap:8px}
.util span{width:36px;height:18px;background:var(--blue-dark);color:#fff;font-size:9px;display:flex;align-items:center;justify-content:center}
.gnav{position:absolute;right:60px;top:50px;display:flex;gap:30px}
.gnav a{text-decoration:none;text-align:center;color:var(--blue-dark);font-family:"Montserrat",sans-serif;font-size:13px;font-weight:600}
.gnav a small{display:block;font-family:"Noto Sans JP",sans-serif;font-size:9px;color:var(--muted);font-weight:400;margin-top:3px}
.gnav a.current{border-bottom:2px solid var(--blue);padding-bottom:4px}

/* hero */
.hero{top:108px;left:0;width:1200px;height:604px;background:linear-gradient(180deg,#7fc4f0 0%,#b9def5 30%,#5aa27e 55%,#2f7fb0 75%,#1d5f8f 100%)}
.hero-copy{position:absolute;right:90px;top:250px;text-align:right;color:#fff;font-family:"Montserrat",sans-serif;font-weight:300;font-size:104px;line-height:1;letter-spacing:2px;text-shadow:0 2px 8px rgba(0,40,80,.35)}
.hero-sub{position:absolute;right:110px;top:535px;color:#fff;font-size:34px;letter-spacing:3px;font-family:"Montserrat",sans-serif;font-weight:400;text-shadow:0 2px 6px rgba(0,40,80,.4)}

/* intro */
.intro{position:absolute;top:712px;left:0;width:1200px;height:228px;text-align:center}
.intro h2{margin-top:58px;font-size:30px;font-weight:700;color:var(--blue);letter-spacing:2px}
.intro .rule{width:640px;height:3px;margin:12px auto 24px;background:linear-gradient(90deg,transparent,var(--sky),transparent)}
.intro p{font-size:15px;line-height:1.9;color:var(--text)}

/* feature panels */
.panel{top:940px;width:600px;height:400px}
.panel-company{left:0;background:linear-gradient(160deg,#9fcbe8,#4f8fb8 60%,#2f6b86)}
.panel-safety{left:600px;background:linear-gradient(160deg,#a7d3f0,#6aa3c8 55%,#3b6f93)}
.ring{position:absolute;width:240px;height:240px;border:2px solid #fff;border-radius:50%;top:1012px}
.panel-title{position:absolute;color:#fff;font-family:"Montserrat",sans-serif;font-size:30px;font-weight:400;letter-spacing:2px}
.panel-text{position:absolute;color:#fff;font-size:13px;line-height:1.7;width:230px}
.more{position:absolute;color:#fff;font-family:"Montserrat",sans-serif;font-size:14px}

/* bus */
.bus-left{top:1470px;left:0;width:600px;height:410px;background:linear-gradient(180deg,#8cc4ea,#c9e2f2 45%,#8a9a8a 70%,#6f7780)}
.bus-right{top:1470px;left:600px;width:600px;height:410px;background:linear-gradient(180deg,#7bb9e6,#b8d9ef 40%,#9aa4ad 65%,#5f666d)}
.bus-badge{position:absolute;left:462px;top:1300px;width:276px;height:276px;border-radius:50%;background:#fff;border:3px solid var(--teal);text-align:center;box-shadow:0 0 0 10px rgba(255,255,255,.8)}
.bus-badge .en{display:block;margin-top:78px;color:var(--teal);font-size:30px;font-weight:600;letter-spacing:3px}
.bus-badge small{display:block;color:var(--teal);font-size:13px;margin-top:8px}
.bus-badge .line{width:80px;height:2px;background:var(--teal);margin:16px auto 10px}
.bus-badge b{font-family:"Montserrat",sans-serif;color:var(--teal);font-size:14px;font-weight:600}

/* information */
.info{position:absolute;top:1880px;left:0;width:1200px;height:380px}
.info-head{position:absolute;left:172px;top:80px}
.info-head h2{font-family:"Montserrat",sans-serif;color:var(--blue);font-size:32px;font-weight:600;letter-spacing:2px}
.info-head p{font-size:14px;color:var(--muted);margin-top:10px;padding-left:8px}
.info-line{position:absolute;left:0;top:170px;width:440px;height:1px;background:var(--line)}
.news{position:absolute;left:510px;width:620px;border-bottom:1px solid var(--line);padding-bottom:18px;display:flex;gap:28px}
.news time{font-family:"Montserrat",sans-serif;color:var(--blue);font-weight:600;font-size:14px;white-space:nowrap}
.news p{font-size:13px;line-height:1.9;color:var(--text)}

/* contact */
.contact{top:2260px;left:0;width:1200px;height:340px;background:linear-gradient(180deg,#7f9fb5,#5f7d92 45%,#4a5f6e)}
.contact-shade{position:absolute;top:2260px;left:0;width:1200px;height:340px;background:rgba(10,40,70,.25)}
.tel{position:absolute;left:290px;color:#fff;font-family:"Montserrat",sans-serif;font-size:40px;font-weight:400;display:flex;align-items:center;gap:12px;letter-spacing:1px}
.mail-btn{position:absolute;left:640px;top:2420px;width:280px;height:84px;background:var(--blue);color:#fff;display:flex;align-items:center;justify-content:center;gap:16px;font-size:22px;font-weight:500;border-radius:2px}

/* station */
.station{top:2600px;left:0;width:1200px;height:600px;background:linear-gradient(180deg,#4f8fd8 0%,#8cb8e8 35%,#4a5a72 60%,#2b3548 85%,#394256)}

/* footer */
.site-footer{position:absolute;top:3200px;left:0;width:1200px;height:224px;background:var(--blue);color:#fff}
.footer-name{position:absolute;left:180px;top:42px;font-size:26px;font-weight:700;letter-spacing:3px}
.footer-info{position:absolute;left:190px;top:96px;font-size:12px;line-height:2}
.footer-nav{position:absolute;left:850px;top:54px;list-style:none;font-size:12px;line-height:2}
.footer-nav li::before{content:"- ";}
.copy{position:absolute;left:0;bottom:14px;width:1200px;text-align:center;font-size:10px;opacity:.8}
</style>
</head>
<body>

<header class="site-header">
  <div class="brand">ロゴ<br>MARK</div>
  <div class="util"><span>EN</span><span>中文</span><span>한국</span></div>
  <nav class="gnav">
    <a class="current" href="#">HOME<small>ホーム</small></a>
    <a href="#">COMPANY<small>会社概要</small></a>
    <a href="#">BUS<small>車両紹介</small></a>
    <a href="#">SAFETY<small>安全への取組</small></a>
    <a href="#">CONTACT<small>お問合せ</small></a>
  </nav>
</header>

<div class="photo hero" role="img" aria-label="海辺の高層ビル街とヨットハーバーの眺望写真"></div>
<div class="hero-copy">Safety<br>High Quality</div>
<div class="hero-sub">○○○○○○○○ Company Limited</div>

<section class="intro">
  <h2>より一層安全・安心なお客様サービスの実現へ</h2>
  <div class="rule"></div>
  <p>○○○○は、"Safety"と"High Quality"をモットーとし、<br>これからも「確かな安全・安心」と「質高きサービス」で快適な旅をお手伝いします。</p>
</section>

<div class="photo panel panel-company" role="img" aria-label="港と高層ビル群の都市景観写真"></div>
<div class="photo panel panel-safety" role="img" aria-label="港町の街並みと海の俯瞰写真"></div>
<div class="ring" style="left:40px"></div>
<div class="panel-title" style="left:72px;top:1106px">COMPANY</div>
<div class="panel-text" style="left:300px;top:1100px">会社の概要をご案内します。<br>私たちの取り組みとあゆみ。</div>
<div class="more" style="left:150px;top:1200px">MORE &gt;&gt;</div>
<div class="ring" style="left:620px"></div>
<div class="panel-title" style="left:700px;top:1106px">SAFETY</div>
<div class="panel-text" style="left:900px;top:1100px">安全への取り組みをご紹介<br>確かな運行をお約束します。</div>
<div class="more" style="left:730px;top:1200px">MORE &gt;&gt;</div>

<div class="photo bus-left" role="img" aria-label="ヤシの木が並ぶ道路に停まる観光バスの写真"></div>
<div class="photo bus-right" role="img" aria-label="駐車場に並ぶ白い観光バスの写真"></div>
<div class="bus-badge">
  <span class="en">BUS</span>
  <small>車両のご紹介</small>
  <div class="line"></div>
  <b>MORE &gt;&gt;</b>
</div>

<section class="info">
  <div class="info-head">
    <h2>INFORMATION</h2>
    <p>○○○○○○からのお知らせ</p>
  </div>
  <div class="info-line"></div>
  <div class="news" style="top:40px">
    <time>2020/3/1</time>
    <p>テキストが入ります。テキストが入ります。テキストが入ります。テキストが入ります。テキストが入ります。テキストが入ります。テキストが入ります。テキストが入ります。</p>
  </div>
  <div class="news" style="top:150px">
    <time>2020/3/1</time>
    <p>テキストが入ります。テキストが入ります。テキストが入ります。テキストが入ります。テキストが入ります。テキストが入ります。テキストが入ります。テキストが入ります。</p>
  </div>
</section>

<div class="photo contact" role="img" aria-label="駅前を走るバスと街並みの写真"></div>
<div class="contact-shade"></div>
<div class="tel" style="top:2378px">
  <svg width="30" height="30" viewBox="0 0 24 24" fill="#fff"><path d="M6.6 10.8a15 15 0 0 0 6.6 6.6l2.2-2.2a1 1 0 0 1 1-.25 11.4 11.4 0 0 0 3.6.57 1 1 0 0 1 1 1V20a1 1 0 0 1-1 1A17 17 0 0 1 3 4a1 1 0 0 1 1-1h3.5a1 1 0 0 1 1 1c0 1.25.2 2.45.57 3.6a1 1 0 0 1-.25 1z"/></svg>
  012-000-1234
</div>
<div class="tel" style="top:2466px">
  <svg width="30" height="30" viewBox="0 0 24 24" fill="#fff"><path d="M19 8H5a3 3 0 0 0-3 3v6h4v4h12v-4h4v-6a3 3 0 0 0-3-3zm-3 11H8v-5h8zM18 3H6v4h12z"/></svg>
  098-000-5678
</div>
<div class="mail-btn">
  <svg width="28" height="22" viewBox="0 0 24 18" fill="#fff"><path d="M2 0h20a2 2 0 0 1 2 2v14a2 2 0 0 1-2 2H2a2 2 0 0 1-2-2V2a2 2 0 0 1 2-2zm10 9L2 3v2l10 6 10-6V3z"/></svg>
  メールフォーム
</div>

<div class="photo station" role="img" aria-label="夕暮れの駅前ロータリーと高層ビル群の写真"></div>

<footer class="site-footer">
  <div class="footer-name">○○○○○○○株式会社</div>
  <div class="footer-info">〒000-0000　○○県○○市○○町1-2-3<br>TEL　012-000-1234<br>FAX　098-000-5678</div>
  <ul class="footer-nav">
    <li>ホーム</li>
    <li>会社概要</li>
    <li>車両紹介</li>
    <li>安全への取組</li>
    <li>お問い合わせ</li>
  </ul>
  <div class="copy">Copyright © ○○○○○○ All Rights Reserved.</div>
</footer>

</body>
</html>
```